Banner/Sign artwork for sign shop

We're after a clean, modern almost minimalist sign design for across the front of our new shop. Size is approximately 5.3m wide x 3m high.
We're a small sign & print shop looking to attract larger corporate customers. Sign to consist of our contact details, maybe a slogan? and some icons of products we supply. Ie: a-frames, banners, flags, vehicle signage etc etc. Our colours are orange, black and white. Would really like a catchy graphic or similar for passers by to notice as there is a lot of traffic during the day.
Please not a busy or crowded design.
Will be carrying this style through on additional signage, cards, flyers etc.
Horizontal and stacked NEW logo attached.
Photo of where this sign is to go. Awning will already have our logo... new sign to go underneath where the pink section is (and carried around the side).

Looking forward to working with you!

• Our contact details - phone, website and KD logo
Clean professional look to show we're not an unprofessional backyard type of shop
We are on a main road, so the layout can't be "busy". must be easy to read.

PLEASE READ DESCRIPTION
• Icons for products?
Would be great to have a graphic, or set of graphics we can use on future signage and advertising. We have pixelvaultz account, so feel free to grab anything from there and we can then download the high res file.
• Logo DOESN'T need to appear on banner, as it's on shop awning above!
Can't be too busy with information.
Can't have really small text

```html
<!DOCTYPE html>
<html lang="en">
<head>
<meta charset="utf-8">
<title>SignForge Shopfront Banner</title>
<link rel="stylesheet" href="https://fonts.googleapis.com/css2?family=Montserrat:wght@500;700;800&display=swap">
<style>
  :root {
    --page-bg: #f4f4f4;
    --banner-black: #0b0b0c;
    --stripe-grey: #26262c;
    --orange: #f26a21;
    --amber: #f9a11b;
    --white: #ffffff;
  }
  html, body {
    margin: 0;
    padding: 0;
    width: 1200px;
    height: 2561px;
    overflow: hidden;
    background: var(--page-bg);
  }
  .shopfront-banner {
    position: absolute;
    left: 104px;
    top: 1855px;
    width: 993px;
    height: 562px;
    box-shadow: 0 8px 22px rgba(0,0,0,0.25);
  }
  .shopfront-banner svg { display: block; }
  .headline {
    font-family: "Montserrat", sans-serif;
    font-weight: 800;
    font-size: 80px;
    fill: var(--white);
  }
  .supply-label {
    font-family: "Montserrat", sans-serif;
    font-weight: 800;
    font-size: 40px;
    fill: var(--orange);
    letter-spacing: 1px;
  }
  .phone-number {
    font-family: "Montserrat", sans-serif;
    font-weight: 700;
    font-size: 62px;
    fill: var(--white);
  }
  .web-address {
    font-family: "Montserrat", sans-serif;
    font-weight: 500;
    font-size: 50px;
    fill: var(--white);
    letter-spacing: 1px;
  }
  .social-handle {
    font-family: "Montserrat", sans-serif;
    font-weight: 800;
    font-size: 34px;
    fill: var(--orange);
  }
  .product-badge { fill: none; stroke: var(--white); stroke-width: 2.5; }
  .product-icon { fill: none; stroke: var(--white); stroke-width: 2.4; stroke-linejoin: round; stroke-linecap: round; }
</style>
</head>
<body>
  <div class="shopfront-banner">
    <svg width="993" height="562" viewBox="0 0 993 562" xmlns="http://www.w3.org/2000/svg">
      <rect class="banner-field" width="993" height="562" fill="var(--banner-black)"/>

      <g class="accent-stripes">
        <polygon points="0,0 120,0 0,120" fill="var(--orange)"/>
        <polygon points="145,0 185,0 0,185 0,145" fill="var(--stripe-grey)"/>
        <polygon points="993,562 873,562 993,442" fill="var(--amber)"/>
        <polygon points="848,562 808,562 993,377 993,417" fill="var(--stripe-grey)"/>
      </g>

      <text class="headline" x="496" y="130" text-anchor="middle">WELCOME TO</text>
      <text class="headline" x="496" y="202" text-anchor="middle">SIGNFORGE</text>

      <text class="social-handle" x="918" y="124" text-anchor="middle">KD</text>

      <text class="supply-label" x="496" y="286" text-anchor="middle">WE SUPPLY</text>

      <g class="product-icons">
        <g transform="translate(393 336)">
          <circle class="product-badge" r="27"/>
          <rect class="product-icon" x="-13" y="-10" width="26" height="20"/>
          <path class="product-icon" d="M-10 6 L-3 -1 L2 4 L6 0 L10 5"/>
        </g>
        <g transform="translate(462 336)">
          <circle class="product-badge" r="27"/>
          <path class="product-icon" d="M-10 -12 H10 M-9 -12 L-13 14 M9 -12 L13 14 M-10 -2 H10"/>
        </g>
        <g transform="translate(531 336)">
          <circle class="product-badge" r="27"/>
          <path class="product-icon" d="M-9 15 V-14 M-9 -13 H11 V1 H-9"/>
        </g>
        <g transform="translate(600 336)">
          <circle class="product-badge" r="27"/>
          <path class="product-icon" d="M0 -15 V15 M-11 -10 H11 V-2 H-11 Z M-11 2 H11 V10 H-11 Z"/>
        </g>
      </g>

      <text class="phone-number" x="496" y="470" text-anchor="middle">987-6543-210</text>
      <text class="web-address" x="496" y="520" text-anchor="middle">www.signforge.com</text>
    </svg>
  </div>
</body>
</html>
```